Redesign of Engineering firm website

I want a redesign of the velkorpower.com website with the below in mind:

1- the client has a 3 main sectors: Renewable Energy, Process Automation and General Engineering.
2- Home page should show the 3 sectors
3- the other standard pages should be home, About, Clients, Projects, Training, Career, and Contact
4- The theme should be wordpress.
5- Responsive layout that works with all devices
6- One page layout is preferable for the home page.
7- it should be original and is not copied from other templates.

Target Market(s)

Engineers and professional

Industry/Entity Type

Solar Energy

Font styles to use
Serif
Sans Serif

Colors
3277b5
0355a3
0493ce

Requirements
Must have
• pictures that represent the three sectors

```html
<!DOCTYPE html>
<html lang="en">
<head>
<meta charset="utf-8">
<title>Velkor Power – Renewable Energy, Process Automation, General Engineering</title>
<link href="https://fonts.googleapis.com/css2?family=Open+Sans:wght@300;400;600;700&display=swap" rel="stylesheet">
<style>
:root{
  --yellow:#ffcc00;
  --yellow-dark:#e6b800;
  --blue:#0088b0;
  --blue-deep:#0a7ca6;
  --ink:#1a1a1a;
  --text:#555;
  --muted:#bbb;
  --line:#e6e6e6;
  --footer:#0e2a35;
  --footer-line:#22424e;
  --footer-text:#9fb1b8;
  --white:#fff;
}
*{box-sizing:border-box;margin:0;padding:0}
html,body{width:1200px;height:3044px;overflow:hidden;background:var(--white)}
body{font-family:"Open Sans",Arial,sans-serif;color:var(--text);position:relative}
.abs{position:absolute}
.center{text-align:center}
.btn{position:absolute;background:var(--yellow);color:var(--ink);font-size:10px;font-weight:700;text-transform:uppercase;display:flex;align-items:center;justify-content:center;letter-spacing:.2px}

/* header */
.site-header{position:absolute;left:0;top:0;width:1200px;height:73px;background:var(--white)}
.brand{position:absolute;left:162px;top:10px;font-size:40px;font-weight:700;color:var(--blue);letter-spacing:-1px;line-height:48px;display:flex;align-items:center;gap:8px}
.brand .dot{width:10px;height:10px;background:var(--yellow)}
.contact-chip{position:absolute;top:16px;display:flex;align-items:center;gap:12px}
.contact-chip .ring{width:38px;height:38px;border:2px solid #d8d8d8;border-radius:50%;display:flex;align-items:center;justify-content:center}
.contact-chip .label{font-size:15px;color:#888;line-height:18px}
.contact-chip .value{font-size:15px;font-weight:700;color:var(--blue);line-height:20px}
.contact-chip .small{font-size:11px;color:#666;line-height:18px}

/* nav */
.main-nav{position:absolute;left:0;top:73px;width:1200px;height:49px;background:var(--yellow)}
.main-nav a{position:absolute;top:0;height:49px;line-height:49px;font-size:13px;color:#333;text-decoration:none;transform:translateX(-50%)}
.main-nav .active{background:var(--yellow-dark);color:var(--white);width:113px;text-align:center;transform:none;left:165px}
.main-nav .sep{position:absolute;top:0;width:1px;height:49px;background:#f0c000}

/* hero */
.hero{position:absolute;left:0;top:122px;width:1200px;height:449px;background:linear-gradient(180deg,#3b4650 0%,#4d5a4a 45%,#3e5a3a 70%,#2c3a52 100%)}
.hero h1{position:absolute;left:0;width:1200px;top:122px;font-size:26px;font-weight:700;color:var(--white);text-align:center}
.hero p{position:absolute;left:270px;width:660px;top:180px;font-size:11.5px;font-weight:700;color:var(--white);text-align:center;line-height:20px}
.hero .arrow{position:absolute;top:183px;width:43px;height:35px;background:var(--yellow);display:flex;align-items:center;justify-content:center}
.hero .dots{position:absolute;left:586px;top:358px;display:flex;gap:7px}
.hero .dots i{width:5px;height:5px;background:var(--white)}
.hero .dots i:first-child{background:var(--yellow)}

/* headings */
.sec-title{position:absolute;left:0;width:1200px;text-align:center;font-size:19px;font-weight:600;color:var(--ink);text-transform:uppercase}
.sec-sub{position:absolute;left:0;width:1200px;text-align:center;font-size:11px;color:var(--muted);text-transform:uppercase}

.about-text{position:absolute;left:160px;width:890px;font-size:10.5px;line-height:18px;text-align:center;color:#555}

/* stats */
.stats{position:absolute;left:0;top:875px;width:1200px;height:132px;background:var(--blue)}
.stat{position:absolute;top:28px;color:var(--white)}
.stat b{display:block;font-size:44px;font-weight:400;line-height:50px}
.stat span{font-size:10px;font-weight:600;text-transform:uppercase}

/* cards */
.card{position:absolute;width:278px;background:var(--white);box-shadow:0 0 6px rgba(0,0,0,.12)}
.card h3{position:absolute;left:0;width:100%;text-align:center;font-size:19px;font-weight:400;text-transform:uppercase}
.card p{position:absolute;left:36px;width:206px;text-align:justify;text-align-last:center;font-size:10.5px;line-height:18px;color:#777}
.service h3{color:var(--blue);top:96px}
.service .icon{position:absolute;left:114px;top:28px}

/* filters */
.filter{position:absolute;top:1570px;height:26px;border:1.5px solid #333;font-size:10px;color:#333;display:flex;align-items:center;justify-content:center;text-transform:uppercase}
.filter.on{background:var(--yellow);border-color:var(--yellow);font-weight:600}

.photo{position:absolute;width:278px;height:210px}
.overlay{background:rgba(10,14,18,.85)}
.overlay h4{position:absolute;top:60px;width:100%;text-align:center;color:var(--white);font-size:13px;font-weight:700}
.overlay p{position:absolute;top:90px;left:45px;width:188px;text-align:center;color:var(--white);font-size:10px;line-height:18px}
.overlay .plus{position:absolute;left:129px;top:147px;width:20px;height:16px;background:var(--white);color:#333;font-size:11px;line-height:16px;text-align:center}

.training h3{top:204px;color:var(--ink)}
.training .pic{position:absolute;left:15px;top:15px;width:248px;height:157px}

/* footer */
.site-footer{position:absolute;left:0;top:2627px;width:1200px;height:417px;background:var(--footer)}
.site-footer .brand{left:162px;top:68px;font-size:32px}
.foot-about{position:absolute;left:162px;top:139px;width:202px;font-size:10.5px;line-height:18px;color:var(--footer-text);text-align:justify}
.foot-chip{position:absolute;top:45px;display:flex;align-items:center;gap:10px;color:var(--footer-text);font-size:11px;line-height:18px}
.foot-chip .ring{width:38px;height:38px;border:2px solid #4a6570;border-radius:50%;display:flex;align-items:center;justify-content:center}
.foot-chip b{font-weight:700}
.foot-rule{position:absolute;left:437px;top:103px;width:601px;height:1px;background:var(--footer-line)}
.foot-head{position:absolute;top:122px;font-size:19px;font-weight:700;color:var(--blue)}
.foot-list{position:absolute;top:158px;list-style:none}
.foot-list li{font-size:10.5px;color:var(--footer-text);height:30px;display:flex;align-items:flex-start;gap:8px}
.foot-list li::before{content:"";width:5px;height:5px;border-radius:50%;background:var(--blue);margin-top:6px}
.email-field{position:absolute;left:836px;top:216px;width:202px;height:32px;background:#1f4656;color:#5f8794;font-size:10px;padding:10px 16px}
.subscribe{position:absolute;left:836px;top:257px;width:202px;height:32px;background:var(--blue);color:var(--white);font-size:10px;font-weight:600;display:flex;align-items:center;justify-content:center}
.copyright{position:absolute;left:0;width:1200px;top:376px;text-align:center;font-size:10px;color:var(--footer-text)}
</style>
</head>
<body>

<header class="site-header">
  <div class="brand">VELKOR<span class="dot"></span></div>
  <div class="contact-chip" style="left:540px">
    <div class="ring"><svg width="16" height="16" viewBox="0 0 16 16"><rect x="1" y="1" width="14" height="14" rx="3" fill="#0088b0"/><path d="M5 4.5c.3 3 2.5 5.6 6 6.5l.6-1.6-1.6-.8-.8.9c-1-.5-1.8-1.3-2.3-2.3l.9-.8-.8-1.6z" fill="#fff"/></svg></div>
    <div><div class="label">Call Us</div><div class="value">+966135550142</div></div>
  </div>
  <div class="contact-chip" style="left:735px">
    <div class="ring"><svg width="14" height="18" viewBox="0 0 14 18"><path d="M7 1a5 5 0 0 0-5 5c0 4 5 10 5 10s5-6 5-10a5 5 0 0 0-5-5z" fill="#0088b0"/><circle cx="7" cy="6" r="1.8" fill="#fff"/></svg></div>
    <div><div class="value">Harbor District&nbsp; Eastern Province 31800</div><div class="small">Kingdom of Saudi Arabia</div></div>
  </div>
</header>

<nav class="main-nav">
  <a class="active">Home</a>
  <span class="sep" style="left:278px"></span>
  <a style="left:343px">About</a>
  <span class="sep" style="left:401px"></span>
  <a style="left:462px">Clients</a>
  <span class="sep" style="left:527px"></span>
  <a style="left:587px">Projects</a>
  <span class="sep" style="left:648px"></span>
  <a style="left:718px">Training</a>
  <span class="sep" style="left:784px"></span>
  <a style="left:843px">Career</a>
  <span class="sep" style="left:905px"></span>
  <a style="left:967px">Contact</a>
  <span class="sep" style="left:1026px"></span>
</nav>

<section class="hero" role="img" aria-label="Wind turbines on green hills above a field of solar panels, darkened">
  <h1>VELKORPOWER</h1>
  <p>WE ARE THE SOLAR EXPERTS IN THE SOLAR KINGDOM. THE KSA (SAUDI ARABIA) SOLAR MARKET IS A PROMISING MARKET WITH HUGE POTENTIAL. THE PLAN IS TO BUILD 41,000 MW OF SOLAR IN THE COMING 20 YEARS, AS ANNOUNCED BY N.R.E.A (NATIONAL RENEWABLE ENERGY AUTHORITY).</p>
  <div class="arrow" style="left:119px"><svg width="12" height="10" viewBox="0 0 12 10"><rect x="0" y="0" width="2" height="10" fill="#222"/><path d="M7 0v10L2 5zM12 0v10L7 5z" fill="#222"/></svg></div>
  <div class="arrow" style="left:1038px"><svg width="12" height="10" viewBox="0 0 12 10"><rect x="10" y="0" width="2" height="10" fill="#222"/><path d="M0 0v10l5-5zM5 0v10l5-5z" fill="#222"/></svg></div>
  <div class="btn" style="left:540px;top:260px;width:121px;height:30px">Learn More</div>
  <div class="dots"><i></i><i></i><i></i></div>
</section>

<section class="about">
  <h2 class="sec-title" style="top:612px">About</h2>
  <p class="about-text" style="top:653px">Lorem ipsum dolor sit amet, consectetur adipiscing elit. Duis tincidunt varius lacus eu dapibus. Nullam mattis tempus leo ut interdum. Donec tincidunt augue tincidunt varius volutpat. Vestibulum nec luctus tortor, id ultrices ipsum. Maecenas sed sodales ligula, sed tincidunt lorem. Cras a porttitor metus, et elementum ligula. Maecenas suscipit lorem pulvinar luctus rutrum. Aenean ac nibh purus. Vestibulum ultrices, nisi vitae euismod convallis, diam purus placerat purus, a tempus ipsum magna at nibh.</p>
  <p class="about-text" style="top:725px">Nulla viverra imperdiet fringilla. Suspendisse tristique pellentesque mauris, id tincidunt tortor laoreet quis. Quisque molestie ultrices nisi, sit amet pretium ante condimentum ut. Sed iaculis lectus odio, mattis aliquet odio rhoncus in. Maecenas ornare, ligula sed porttitor aliquet, enim augue porta dui, egestas efficitur erat elit nec risus. Aliquam erat volutpat.</p>
  <div class="btn" style="left:540px;top:791px;width:121px;height:30px">Learn More</div>
</section>

<section class="stats">
  <div class="stat" style="left:199px"><b>20 +</b><span>Years Experience</span></div>
  <div class="stat" style="left:402px"><b>200 +</b><span>Good Engineer</span></div>
  <div class="stat" style="left:625px"><b>300 +</b><span>Customer</span></div>
  <div class="stat" style="left:874px"><b>220 +</b><span>Projects Complete</span></div>
</section>

<section class="services">
  <h2 class="sec-title" style="top:1066px">Our Services in Renewable Include</h2>
  <div class="sec-sub" style="top:1101px">Different Services</div>

  <article class="card service" style="left:161px;top:1148px;height:301px">
    <svg class="icon" width="50" height="54" viewBox="0 0 50 54" fill="none" stroke="#0088b0" stroke-width="2.4"><circle cx="25" cy="20" r="17"/><circle cx="25" cy="20" r="7"/><path d="M25 8v5M25 27v5M13 20h5M32 20h5M17 12l3 3M30 25l3 3M33 12l-3 3M20 25l-3 3"/><path d="M18 37h14M19 42h12M21 47h8M25 47v5"/></svg>
    <h3>Renewable Energy</h3>
    <p style="top:137px">Lorem Ipsum has been the industry's standard dummy text ever since the 1500s, when an unknown printer took a galley of type and scrambled it to make a type specimen book.</p>
    <div class="btn" style="left:85px;top:244px;width:107px;height:28px">Learn More</div>
  </article>

  <article class="card service" style="left:461px;top:1148px;height:301px">
    <svg class="icon" width="50" height="50" viewBox="0 0 50 50"><path d="M21 2h8l1 6 5 2 5-4 6 6-4 5 2 5 6 1v8l-6 1-2 5 4 5-6 6-5-4-5 2-1 6h-8l-1-6-5-2-5 4-6-6 4-5-2-5-6-1v-8l6-1 2-5-4-5 6-6 5 4 5-2z" fill="#0088b0"/><circle cx="25" cy="25" r="12" fill="#fff"/><path d="M21 18v14l11-7z" fill="#0088b0"/></svg>
    <h3>Process Automation</h3>
    <p style="top:137px">Lorem Ipsum has been the industry's standard dummy text ever since the 1500s, when an unknown printer took a galley of type and scrambled it to make a type specimen book.</p>
    <div class="btn" style="left:85px;top:244px;width:107px;height:28px">Learn More</div>
  </article>

  <article class="card service" style="left:760px;top:1148px;height:301px">
    <svg class="icon" width="50" height="50" viewBox="0 0 50 50" fill="#0088b0"><path d="M13 17a12 12 0 0 1 24 0z"/><rect x="10" y="17" width="30" height="3"/><rect x="23" y="4" width="4" height="6" fill="#fff"/><path d="M2 50c0-11 9-17 23-17s23 6 23 17z"/><circle cx="25" cy="25" r="8"/><path d="M21 34l4 9 4-9z" fill="#fff"/></svg>
    <h3>General Engineering</h3>
    <p style="top:137px">Lorem Ipsum has been the industry's standard dummy text ever since the 1500s, when an unknown printer took a galley of type and scrambled it to make a type specimen book.</p>
    <div class="btn" style="left:85px;top:244px;width:107px;height:28px">Learn More</div>
  </article>
</section>

<section class="projects">
  <h2 class="sec-title" style="top:1495px">Our Projects</h2>
  <div class="sec-sub" style="top:1530px">Different Services</div>
  <div class="filter on" style="left:304px;width:61px">All</div>
  <div class="filter" style="left:379px;width:93px">Household</div>
  <div class="filter" style="left:485px;width:103px">Organization</div>
  <div class="filter" style="left:600px;width:83px">Research</div>
  <div class="filter" style="left:699px;width:82px">School</div>
  <div class="filter" style="left:795px;width:100px">Solar Energy</div>

  <div class="photo overlay" style="left:161px;top:1628px" role="img" aria-label="Rooftop solar panel rows under a dark overlay">
    <h4>LOREM IPSUM</h4>
    <p>Lorem Ipsum is simply dummy text of the printing and typesetting industry.</p>
    <div class="plus">+</div>
  </div>
  <div class="photo" style="left:461px;top:1628px;background:linear-gradient(135deg,#8a8f96,#c9ccd0 50%,#6d7278)" role="img" aria-label="Technicians in clean suits assembling a satellite solar array"></div>
  <div class="photo" style="left:760px;top:1628px;background:linear-gradient(180deg,#b9c6d4 0%,#8aa0b8 40%,#2d4d86 75%,#9aa3ad)" role="img" aria-label="Workers carrying solar panels on a rooftop"></div>
  <div class="photo" style="left:161px;top:1861px;background:linear-gradient(160deg,#5a4a3e,#2b5aa0 50%,#8b4a36)" role="img" aria-label="Installers fitting solar panels on a tiled roof"></div>
  <div class="photo" style="left:461px;top:1861px;background:linear-gradient(180deg,#c6d6e6 0%,#dfe6ec 50%,#5a6e8c 62%,#b49a78 80%)" role="img" aria-label="Ground-mounted solar arrays in a dry field"></div>
  <div class="photo" style="left:760px;top:1861px;background:linear-gradient(180deg,#dbe4ee 0%,#a8b8c8 40%,#3f5a3a 75%,#4a4d52)" role="img" aria-label="Solar-powered street lights along a tree-lined road"></div>
</section>

<section class="training-sec">
  <h2 class="sec-title" style="top:2110px">Training</h2>
  <div class="sec-sub" style="top:2146px;text-transform:none;font-weight:300">Lorem Ipsum is simply dummy text of the printing and typesetting industry.</div>

  <article class="card training" style="left:161px;top:2193px;height:398px">
    <div class="pic" style="background:linear-gradient(180deg,#4d6b3e 0%,#7a8c6a 40%,#2f58a0 70%,#7a9ac0)" role="img" aria-label="Trainee in safety harness working on rooftop solar panels"></div>
    <h3>Lorem Ipsum</h3>
    <p style="top:234px">Lorem Ipsum has been the industry's standard dummy text ever since the 1500s, when an unknown printer took a galley of type and scrambled it to make a type specimen book.</p>
    <div class="btn" style="left:85px;top:342px;width:107px;height:26px">Learn More</div>
  </article>
  <article class="card training" style="left:461px;top:2193px;height:398px">
    <div class="pic" style="background:linear-gradient(180deg,#6aa0d8 0%,#c8dcf0 40%,#3560a8 65%,#dfe3e8)" role="img" aria-label="Technician kneeling beside solar panels on a flat roof"></div>
    <h3>Lorem Ipsum</h3>
    <p style="top:234px">Lorem Ipsum has been the industry's standard dummy text ever since the 1500s, when an unknown printer took a galley of type and scrambled it to make a type specimen book.</p>
    <div class="btn" style="left:85px;top:342px;width:107px;height:26px">Learn More</div>
  </article>
  <article class="card training" style="left:760px;top:2193px;height:398px">
    <div class="pic" style="background:linear-gradient(135deg,#d4d8dc 0%,#7f8a95 40%,#5a4a40 70%,#a0583e)" role="img" aria-label="Installer lifting a solar panel onto a tiled roof"></div>
    <h3>Lorem Ipsum</h3>
    <p style="top:234px">Lorem Ipsum has been the industry's standard dummy text ever since the 1500s, when an unknown printer took a galley of type and scrambled it to make a type specimen book.</p>
    <div class="btn" style="left:85px;top:342px;width:107px;height:26px">Learn More</div>
  </article>
</section>

<footer class="site-footer">
  <div class="brand">VELKOR<span class="dot"></span></div>
  <p class="foot-about">Lorem Ipsum is simply dummy text of the printing and typesetting industry. Lorem Ipsum has been the industry's standard dummy text ever since the 1500s, when an unknown printer took a galley of type and scrambled it to make a type specimen book.</p>

  <div class="foot-chip" style="left:437px">
    <div class="ring"><svg width="15" height="15" viewBox="0 0 16 16"><rect x="1" y="1" width="14" height="14" rx="3" fill="#9fb1b8"/><path d="M5 4.5c.3 3 2.5 5.6 6 6.5l.6-1.6-1.6-.8-.8.9c-1-.5-1.8-1.3-2.3-2.3l.9-.8-.8-1.6z" fill="#0e2a35"/></svg></div>
    <div>Call Us<br>+966135550142</div>
  </div>
  <div class="foot-chip" style="left:613px">
    <div class="ring"><svg width="13" height="17" viewBox="0 0 14 18"><path d="M7 1a5 5 0 0 0-5 5c0 4 5 10 5 10s5-6 5-10a5 5 0 0 0-5-5z" fill="none" stroke="#9fb1b8" stroke-width="1.6"/><circle cx="7" cy="6" r="1.6" fill="#9fb1b8"/></svg></div>
    <div><b>Harbor District Eastern Province</b><br>31800 Kingdom of Saudi Arabia</div>
  </div>
  <div class="foot-chip" style="left:836px">
    <div class="ring"><svg width="16" height="12" viewBox="0 0 16 12" fill="none" stroke="#9fb1b8" stroke-width="1.5"><rect x="1" y="1" width="14" height="10" rx="1"/><path d="M1 2l7 5 7-5"/></svg></div>
    <div><b>Email</b><br>info@velkorpower.com</div>
  </div>
  <div class="foot-rule"></div>

  <h4 class="foot-head" style="left:438px">QUICKLINK</h4>
  <ul class="foot-list" style="left:438px">
    <li>Home</li><li>About</li><li>Clients</li><li>Projects</li><li>Training</li><li>Career</li>
  </ul>
  <h4 class="foot-head" style="left:611px">CUSTOMER CARE</h4>
  <ul class="foot-list" style="left:611px">
    <li>Customer Service</li><li>Warranty Policy</li><li>Installation and Use</li><li>Contact Us</li>
  </ul>
  <h4 class="foot-head" style="left:836px">NEWSLETTER</h4>
  <p class="abs" style="left:836px;top:159px;width:160px;font-size:10.5px;line-height:18px;color:var(--footer-text)">Sign up for our newsletter and follow us on social media</p>
  <div class="email-field">Email</div>
  <div class="subscribe">SUBSCRIBE</div>
  <div class="copyright">Copyright 2017 velkorpower | All Rights Reserved</div>
</footer>

</body>
</html>
```